Best-selling business author needs Next Craft Line book cover designs

We're launching a series of books and online training videos badged under the "Brightfork Notes - Next Craft Line" brand. The idea is that there are titles for each of the future skills that people will need to survive the robots in the future, eg, Creativity, Critical Thinking Skills, Problem Solving, etc. The exciting job here is to create a series thematic look, and a specific design for the first title, Sharp Prompts.
Hope my brief challenges you, and look forward to your questions and designs.

Target Market(s)

start ups and corporate market (mainly in Asia Pacific) looking to upskill themselves. Probably 18-45 age group, including uni business students, and people working in Meridian 400s.

Industry/Entity Type

Publishing Company

Font styles to use
Serif
Sans Serif
Other font styles liked:
• Felt marker or other 'handcrafted' styles because these will be 'workbook' style publications

Colors
ec1f27
3276b5
00a990
9bcb3c
fbed22
f78f20
6b449b

Requirements
Must have
• Must look professional but not boring or old school.
• Use the "Brightfork Notes Next Craft Line" (logo attached).
• Need category, ie "critical thinking" associated with logo above
• Need title and subtitle of the book, ie "SHARP PROMPTS. How to shape better questions to create explosive breakthroughs."
• All the type you see on sample design, ie reviewers blurb at top, author's name etc.
• Vivid and strong colour schemes to be eye -catching individually but especially strong when lined up on bookshelves together.
• See examples attached for QTV series (competitor) and also a quick design hack by myself to give an idea of what it "might" look like.
• A5 portrait format.
• Spine and Back page will be largely text (with barcode, see example).
• Back page text:
• Heading: Ways to Win the Modern Market with Bold Inquiry Habits.
• - Find out the Sharp Prompts that kick-started empires like NestLoop, Colby Hensel, Beanrowe, Vitalume, Sky Orin, Melodex, Zentrix, Orbely, Tobin Wexley, and even Fundquill.
• - Learn how companies like R&T, Quince, Varlo, AeroMint, Fablon, Lyra, Caravel R3, Movra, and Tulp use Sharp Prompts to develop blockbuster new products, experiences and marketing messages.
• - How to identify and eradicate your cognitive blindspots.
• - How to create a Curiosity Gap (and why that’s so important).
• - Why it’s important to challenge the Status Quo, and how to do it.
• Heading: What if there was a formula for creating Sharp Prompts? There is!
• Get on board this rocket ship with business creativity expert (and best-selling author) Reg Mannix as he guides you through a proven system for creating more insightful, more powerful questions, which point us toward breakthrough solutions, products, and process innovations.
• For the first time, he shares the Sharp Prompts (Discovery Prompt Building Method) here. The same system that he has taught to senior executives from major corporations such as Norvale Bank, Strivon, KessmarFahr, Medwyn, Tolvax, and many other progressive companies.
• Heading: Praise for Sharp Prompts
• “Really enjoyed Sharp Prompts. Like taking a peek into the minds of some of the greatest innovators right as they were asking these SHARP PROMPTS that prompted them to create history!” Rohan Dutt, Head of R&D, Quartel China.
• “Awesome! It’s a great book, I’m a huge fan of the power of questions.” Gavin Hoskins, VP, Norvale Bank.
• "Sharp Prompts is a Sharp Book! This has really helped with both my classroom sessions and consulting projects. Well done!"
• Martin Esterhal, Adj. Professor, The University of Bramcote.
• www.regmannix.example #sharp prompts
• [insert bar code]
Nice to have
• Prefer simple strong bold graphic approach.
• Using photos, or icons to highlight the topic. Please avoid cliches.
Should not have
• Not overly fancy, ornate, or visually complicated.

```html
<!DOCTYPE html>
<html lang="en">
<head>
<meta charset="utf-8">
<title>Sharp Prompts — Book Cover</title>
<link href="https://fonts.googleapis.com/css2?family=Open+Sans:wght@300;400;600;700;800&display=swap" rel="stylesheet">
<style>
  :root {
    --backdrop: #dfe6ea;
    --paper: #ffffff;
    --brand-red: #c63d31;
    --sticker-orange: #ee7b52;
    --torn-shadow: #e4e4e4;
    --ink-dark: #333333;
    --art-light: #f2f2f2;
    --art-mid: #d9d9d9;
  }
  * { margin: 0; padding: 0; box-sizing: border-box; }
  html, body {
    width: 1200px; height: 1200px; overflow: hidden;
    background: var(--backdrop);
    font-family: "Open Sans", Arial, sans-serif;
  }
  .cover {
    position: absolute; left: 254px; top: 112px;
    width: 693px; height: 976px;
    background: var(--paper);
    box-shadow: 0 10px 30px rgba(0,0,0,0.18);
    overflow: hidden;
  }
  .series-mark {
    position: absolute; left: 482px; top: 30px;
    display: flex; align-items: center; gap: 7px;
  }
  .series-mark__dot {
    width: 16px; height: 16px; border-radius: 50%;
    background: var(--brand-red);
  }
  .series-mark__name {
    font-size: 17px; font-weight: 700; color: var(--ink-dark);
    line-height: 1;
  }
  .series-mark__line {
    position: absolute; left: 505px; top: 52px;
    font-size: 8px; font-weight: 600; letter-spacing: 0.5px;
    color: var(--ink-dark); text-transform: uppercase;
  }
  .cover-art {
    position: absolute; left: 160px; top: 140px;
    width: 420px; height: 300px;
    background: radial-gradient(ellipse at 50% 55%, var(--art-mid) 0%, var(--art-light) 55%, var(--paper) 80%);
  }
  .title-band {
    position: absolute; left: 0; top: 505px;
    width: 693px; height: 370px;
  }
  .category-sticker {
    position: absolute; left: 481px; top: 492px;
    width: 98px; height: 98px; border-radius: 50%;
    background: var(--sticker-orange);
    color: var(--paper);
    display: flex; flex-direction: column; align-items: center; justify-content: center;
    font-size: 19px; font-weight: 400; line-height: 1.15; text-align: center;
  }
  .book-title {
    position: absolute; left: 0; width: 100%; text-align: center;
    color: var(--paper); line-height: 1;
  }
  .book-title--main { top: 548px; font-size: 90px; font-weight: 800; letter-spacing: 1px; }
  .book-title--sub  { top: 648px; font-size: 94px; font-weight: 300; letter-spacing: 1px; }
  .book-subtitle {
    position: absolute; left: 0; top: 760px; width: 100%;
    text-align: center; color: var(--paper);
    font-size: 23px; font-weight: 600; line-height: 32px;
    text-transform: uppercase;
  }
  .author {
    position: absolute; left: 0; top: 882px; width: 100%;
    text-align: center; color: var(--brand-red);
  }
  .author__name { font-size: 36px; font-weight: 700; line-height: 1.1; }
  .author__role { font-size: 19px; font-weight: 600; margin-top: 4px; }
</style>
</head>
<body>
  <main class="cover">
    <div class="series-mark">
      <span class="series-mark__dot"></span>
      <span class="series-mark__name">Brightfork Notes</span>
    </div>
    <div class="series-mark__line">Next Craft Line</div>

    <div class="cover-art" role="img" aria-label="3D illustration of a small white figure flattened under a large red question mark"></div>

    <svg class="title-band" viewBox="0 0 693 370" preserveAspectRatio="none" aria-hidden="true">
      <polygon fill="var(--torn-shadow)" points="0,8 40,2 80,14 130,4 170,18 220,6 260,16 300,2 350,14 400,4 440,16 490,6 540,18 590,2 640,12 693,4 693,366 650,356 600,368 550,354 500,364 450,352 400,366 350,356 300,368 250,354 200,364 150,352 100,366 50,356 0,364"/>
      <polygon fill="var(--brand-red)" points="0,18 30,12 60,22 95,10 130,20 165,12 200,24 240,12 280,22 320,10 360,20 400,12 440,24 480,14 520,22 560,10 600,20 640,12 693,16 693,352 660,346 620,356 580,344 540,354 500,342 460,352 420,344 380,356 340,346 300,356 260,342 220,352 180,344 140,356 100,346 60,354 30,344 0,350"/>
    </svg>

    <div class="category-sticker"><span>Critical</span><span>Thinking</span></div>

    <h1 class="book-title book-title--main">SHARP</h1>
    <div class="book-title book-title--sub">PROMPTS</div>
    <p class="book-subtitle">How to shape better questions<br>to create explosive breakthroughs</p>

    <div class="author">
      <div class="author__name">Reg Mannix</div>
      <div class="author__role">Stagefire MC/Storyteller/Firebrand</div>
    </div>
  </main>
</body>
</html>
```